Book Cover Silencing Gnats, Won'ts and Ifs, Stepping beyond the cycle of sorrow

Need a book cover design for my new web site..Drmarcelbrightly.com (website under construction) I'm appearing on Harbor Lantern Network radio show and want to add a cover design of my book.

My book with enpower people to break the chain of limiting beliefs and unlock their true potential so they will finally experience the life of their dreams

Radio

```html
<!DOCTYPE html>
<html lang="en">
<head>
<meta charset="utf-8">
<title>Silencing Gnats, Won'ts and Ifs — Book Cover</title>
<link rel="stylesheet" href="https://fonts.googleapis.com/css2?family=Inter:wght@200;700&display=swap">
<style>
  :root {
    --paper: #ffffff;
    --teal: #93bdc5;
  }
  html, body {
    margin: 0;
    padding: 0;
    overflow: hidden;
    background: var(--paper);
  }
  .cover {
    position: relative;
    width: 800px;
    height: 1200px;
    background: var(--paper);
    overflow: hidden;
    font-family: "Inter", "Helvetica Neue", Arial, sans-serif;
    color: var(--teal);
  }
  .stripes {
    position: absolute;
    inset: 0;
  }
  .stripes rect { fill: var(--teal); }
  .title {
    position: absolute;
    left: 136px;
    top: 272px;
    margin: 0;
    font-weight: 200;
    font-size: 64px;
    line-height: 64px;
    letter-spacing: -1.5px;
  }
  .title span { display: block; }
  .subtitle {
    position: absolute;
    left: 139px;
    top: 418px;
    margin: 0;
    font-weight: 700;
    font-size: 23px;
    letter-spacing: 0.1px;
  }
  .author {
    position: absolute;
    left: 487px;
    top: 1060px;
    margin: 0;
    font-weight: 700;
    font-size: 26px;
  }
</style>
</head>
<body>
  <main class="cover">
    <svg class="stripes" width="800" height="1200" viewBox="0 0 800 1200" aria-hidden="true">
      <g class="stripes-top">
        <rect x="141" y="0" width="15" height="257"/>
        <rect x="175" y="0" width="19" height="257"/>
        <rect x="214" y="50" width="6" height="207"/>
      </g>
      <g class="stripes-bottom">
        <rect x="141" y="458" width="12" height="643"/>
        <rect x="175" y="458" width="19" height="742"/>
        <rect x="214" y="458" width="6" height="481"/>
      </g>
    </svg>

    <h1 class="title">
      <span>Silencing Gnats,</span>
      <span>Won'ts and Ifs</span>
    </h1>
    <p class="subtitle">Stepping Beyond the Cycle of Sorrow</p>
    <p class="author">Dr. Marcel Brightly</p>
  </main>
</body>
</html>
```